Criação de Kit Layout de Posts para Redes Sociais (Facebook, Instagram e etc) para Decoração & Mobília
" Empresa que desenvolve projetos e instalação de móveis planejados, utilizando o conceito moderno e inovador da marcenaria 4.0. "

```html
<!DOCTYPE html>
<html lang="pt-BR">
<head>
<meta charset="UTF-8">
<title>VERNA Studio de Marcenaria — Horário de funcionamento</title>
<link href="https://fonts.googleapis.com/css2?family=Montserrat:wght@400;500;600;700&display=swap" rel="stylesheet">
<style>
  :root {
    --navy: #1e2747;
    --navy-soft: rgba(30, 39, 71, 0.82);
    --navy-veil: rgba(30, 39, 71, 0.72);
    --salmon-veil: rgba(196, 128, 108, 0.28);
    --gold: #c8a66a;
    --white: #ffffff;
    --wood-light: #d9bf9c;
    --wood-mid: #b48c62;
    --wood-dark: #6e4d33;
  }
  * { margin: 0; padding: 0; box-sizing: border-box; }
  html, body {
    width: 1200px; height: 1200px; overflow: hidden; background: var(--white);
  }
  .post {
    position: relative; width: 1200px; height: 1200px; overflow: hidden;
    font-family: "Montserrat", sans-serif; color: var(--white);
  }
  .workshop-photo {
    position: absolute; inset: 0;
    background:
      radial-gradient(ellipse at 30% 40%, rgba(255,240,220,0.45), transparent 60%),
      linear-gradient(135deg, var(--wood-light) 0%, var(--wood-mid) 55%, var(--wood-dark) 100%);
  }
  .overlays { position: absolute; inset: 0; }
  .hours-box {
    position: absolute; left: 72px; top: 312px; width: 528px; height: 480px;
    background: var(--navy-soft);
  }
  .hours-title {
    position: absolute; left: 98px; top: 355px;
    font-size: 40px; font-weight: 500; line-height: 1.15;
  }
  .hours-title strong { font-weight: 600; text-transform: uppercase; display: block; }
  .hours-days {
    position: absolute; left: 192px; top: 555px;
    font-size: 54px; font-weight: 500;
  }
  .hours-time {
    position: absolute; left: 186px; top: 640px;
    font-size: 24px; font-weight: 500;
  }
  .brand {
    position: absolute; left: 750px; top: 125px;
    display: flex; align-items: center; gap: 22px;
  }
  .brand-mark {
    width: 56px; height: 56px; border: 4px solid var(--gold);
  }
  .brand-name {
    font-size: 82px; font-weight: 500; color: var(--gold);
    letter-spacing: 10px; line-height: 1;
  }
  .brand-tagline {
    position: absolute; left: 830px; top: 222px;
    font-size: 18px; font-weight: 500; letter-spacing: 2px; text-transform: uppercase;
  }
  .contacts {
    position: absolute; left: 420px; top: 962px; list-style: none;
  }
  .contacts li {
    display: flex; align-items: center; height: 62px;
    font-size: 24px; font-weight: 500; letter-spacing: 4px;
  }
  .contacts svg { width: 30px; height: 30px; margin-right: 44px; fill: var(--white); }
</style>
</head>
<body>
<main class="post">
  <div class="workshop-photo" role="img" aria-label="Fotografia de bancada de marcenaria com ferramentas e mão marcando a madeira com lápis"></div>

  <svg class="overlays" width="1200" height="1200" viewBox="0 0 1200 1200" aria-hidden="true">
    <polygon points="408,0 1200,0 1200,790" fill="var(--navy-veil)"/>
    <polygon points="560,820 1200,300 1200,1060" fill="var(--salmon-veil)"/>
    <polygon points="276,1200 720,800 1200,1150 1200,1200" fill="var(--navy)"/>
  </svg>

  <div class="hours-box"></div>
  <h1 class="hours-title"><strong>Nosso horário</strong>de funcionamento:</h1>
  <p class="hours-days">seg à sex</p>
  <p class="hours-time">das 08h00 às 17h00</p>

  <div class="brand">
    <span class="brand-mark"></span>
    <span class="brand-name">VERNA</span>
  </div>
  <p class="brand-tagline">Studio de Marcenaria</p>

  <ul class="contacts">
    <li>
      <svg viewBox="0 0 24 24"><path d="M6.6 10.8a15.1 15.1 0 0 0 6.6 6.6l2.2-2.2a1 1 0 0 1 1-.25 11.4 11.4 0 0 0 3.6.57 1 1 0 0 1 1 1V20a1 1 0 0 1-1 1A17 17 0 0 1 3 4a1 1 0 0 1 1-1h3.5a1 1 0 0 1 1 1c0 1.25.2 2.45.57 3.57a1 1 0 0 1-.25 1z"/></svg>
      +1234-5678
    </li>
    <li>
      <svg viewBox="0 0 24 24"><path d="M12 2a7 7 0 0 0-7 7c0 5.25 7 13 7 13s7-7.75 7-13a7 7 0 0 0-7-7zm0 9.5A2.5 2.5 0 1 1 12 6.5a2.5 2.5 0 0 1 0 5z"/></svg>
      LOREM IPSUM CITY
    </li>
    <li>
      <svg viewBox="0 0 24 24"><path d="M3 5h18a1 1 0 0 1 1 1v12a1 1 0 0 1-1 1H3a1 1 0 0 1-1-1V6a1 1 0 0 1 1-1zm9 7.2L20 7H4z"/></svg>
      LOREM@IPSUM.COM
    </li>
  </ul>
</main>
</body>
</html>
```